Website for boutique digital agency helping high-tech startups accelerate growth.

We need a website design for a relatively young company based in Mauritius called 'LoomTrax'.

We are a professional services firm delivering digital infrastructure for revenue operations (RevOps)*.

Entrepreneurial startups and SMBs in the technology sector work with us to accelerate growth by delivering extraordinary customer experiences across the full customer lifecycle.

We would like a colourful design that utilises the (4) colours of our existing logo design.

The final design should communicate dynamic growth through relentless customer focus.
----------------------------------------------------------
*Revenue Operations (RevOps) is the strategic alignment of sales, marketing and customer success operations to accelerate growth by delivering extraordinary customer experiences across the full customer life cycle.
Updates

Target Market(s)

Entrepreneurial startups and SMBs (Small/Medium Businesses) in the technology sector.

Question: Why the technology sector?

Answer: Because technology entrepreneurs often have a tremendous challenge to effectively communicate to the market and to prospective customers the value and the benefits of their products & services due to the inherent complexity of technological innovation.

LoomTrax is a team of creatively-minded engineers and technologists who have worked with and understand the technologies and innovations our clients are passionate about bringing to market.

Industry/Entity Type

Professional Service

Number of Pages Required

5+ page

Font styles to use
Sans Serif

Requirements
Must have
• Minimalistic designs rich with visual meaning are highly preferred. Mobile responsive designs are also required. Must show how designs render on Desktop, Tablet and Smartphone devices.

Website pages:
1) Homepage: problem statement, target customers, value proposition & benefits
2) Services: 3-4 tiers of services packages with pricing and "how to work with us"
3) Resources: links to all kinds of relevant materials
4) Contact Us: contact form and special project quote form
5) Blog: matrix design with featured images for each post
Nice to have
• Bold, interesting, colourful, inspiring images that visually communicate:
- relentless customer focus
- extraordinary, memorable experiences
- business at the speed of innovation
Should not have
• Any meme or theme that panders to "political correctness".

```html
<!DOCTYPE html>
<html lang="en">
<head>
<meta charset="utf-8">
<title>LoomTrax – Digital Infrastructure for Revenue Operations</title>
<link href="https://fonts.googleapis.com/css2?family=Poppins:wght@500;600;700;800&family=Raleway:wght@400;500;700&display=swap" rel="stylesheet">
<style>
:root{
  --teal:#0d8584;
  --teal-dark:#0b6f71;
  --maroon:#8c3b5e;
  --purple:#5c4a9f;
  --blue:#1e9ce6;
  --green:#4fcf4a;
  --red:#ec3b42;
  --orange:#f07a2a;
  --gray:#8e8e8e;
  --yellow:#e8c22a;
  --ink:#1d1d1d;
  --body:#7a7a7a;
  --footer:#1e1e1e;
  --white:#ffffff;
}
*{box-sizing:border-box;margin:0;padding:0}
html,body{width:1200px;height:5061px;overflow:hidden;background:var(--white)}
body{font-family:"Raleway",sans-serif;color:var(--body);position:relative}
section,header,footer{position:absolute;left:0;width:1200px}
.abs{position:absolute}

/* header */
.site-header{top:0;height:150px;background:var(--white)}
.brand{position:absolute;display:flex;align-items:center;gap:12px;font-family:"Poppins",sans-serif;font-weight:700}
.brand-mark{width:26px;height:26px;background:var(--teal)}
.site-header .brand{left:80px;top:54px;font-size:34px;color:#3a3a3a}
.main-nav{position:absolute;right:62px;top:80px;display:flex;gap:56px;font-family:"Poppins",sans-serif;font-weight:500;font-size:22px;letter-spacing:1px;color:#222}
.search{position:absolute;left:1102px;top:28px}

/* hero */
.hero{top:150px;height:585px;background:linear-gradient(100deg,var(--teal) 0%,#0e8a86 50%,var(--teal-dark) 100%);overflow:hidden}
.hero h1{position:absolute;left:98px;top:170px;font-family:"Poppins",sans-serif;font-weight:700;font-size:47px;line-height:76px;color:var(--white)}
.hero-photo{position:absolute;left:0;top:0}
.slider-arrow{position:absolute;top:253px;width:44px;height:78px;background:#151515;display:flex;align-items:center;justify-content:center}
.slider-arrow.prev{left:0}
.slider-arrow.next{right:0}

/* shared */
.section-title{position:absolute;font-family:"Poppins",sans-serif;font-weight:800;font-size:60px;line-height:74px;color:var(--ink)}
.lead{position:absolute;font-size:23px;line-height:33px;color:var(--body)}
.lifecycle-label{position:absolute;font-family:"Poppins",sans-serif;font-weight:600;font-size:12px;letter-spacing:1px;color:#666;display:flex;align-items:center;gap:8px}
.feature{position:absolute;width:330px}
.feature svg{display:block}
.feature h3{font-family:"Raleway",sans-serif;font-weight:700;font-size:23px;line-height:30px;color:var(--ink);margin-top:38px}
.feature p{font-size:22px;line-height:36px;color:var(--body);margin-top:20px;padding-left:4px}
.feature .more{display:block;margin-top:16px;font-family:"Poppins",sans-serif;font-weight:500;font-size:20px;color:var(--red)}

/* problem */
.problem{top:735px;height:1200px}
.stage{position:absolute;top:227px;width:157px}
.stage .top{height:169px;color:var(--white);font-family:"Poppins",sans-serif;font-weight:600;font-size:21px;line-height:26px;display:flex;align-items:center;justify-content:center;text-align:center}
.stage .bottom{height:41px;background:var(--gray);color:#eee;font-size:13px;display:flex;align-items:center;justify-content:center}
.flow-arrow{position:absolute;top:312px}

/* target */
.target{top:1935px;height:832px;background:linear-gradient(90deg,#7e2f52 0%,var(--maroon) 60%,#9a4a6c 100%)}
.target-photo{position:absolute;left:59px;top:104px;width:518px;height:622px;background:linear-gradient(160deg,#4b5a6e 0%,#7d6a5a 45%,#3f5d86 100%)}
.target h2{position:absolute;left:621px;top:124px;font-family:"Poppins",sans-serif;font-weight:800;font-size:58px;line-height:74px;color:var(--white)}
.target p{position:absolute;left:621px;top:294px;width:520px;font-size:22.5px;line-height:34.6px;color:var(--white);text-align:justify}

/* value */
.value{top:2767px;height:1161px}
.cycle-box{position:absolute;color:var(--white);font-family:"Poppins",sans-serif;font-weight:600;display:flex;align-items:center;justify-content:center}

/* benefits */
.benefits{top:3928px;height:864px;background:var(--yellow)}
.benefits h2{position:absolute;left:0;width:1200px;top:102px;text-align:center;font-family:"Poppins",sans-serif;font-weight:700;font-size:74px;color:var(--white)}
.benefit-card{position:absolute;background:var(--white);border:1px solid #ccc;text-align:center;padding:0 26px}
.benefit-card h3{font-family:"Poppins",sans-serif;font-weight:600;font-size:32px;color:var(--ink);margin-top:64px}
.benefit-card p{font-size:23px;line-height:37px;color:var(--body);margin-top:18px}
.card-arrow{position:absolute;top:689px;width:80px;height:80px;background:#111;display:flex;align-items:center;justify-content:center}

/* footer */
.site-footer{top:4792px;height:269px;background:var(--footer)}
.site-footer .brand{left:65px;top:115px;font-size:38px;color:var(--white)}
.foot-nav{position:absolute;right:61px;top:82px;display:flex;gap:42px;font-family:"Poppins",sans-serif;font-size:23px;color:var(--white)}
.copy{position:absolute;right:61px;top:150px;font-family:"Poppins",sans-serif;font-size:20px;color:#cfcfcf}
</style>
</head>
<body>

<header class="site-header">
  <div class="brand"><span class="brand-mark"></span>loomtrax.io</div>
  <nav class="main-nav"><span>HOME</span><span>SERVICES</span><span>RESOURCES</span><span>BLOG</span><span>CONTACT US</span></nav>
  <svg class="search" width="24" height="24" viewBox="0 0 24 24"><circle cx="10" cy="10" r="7" fill="none" stroke="#777" stroke-width="2.5"/><line x1="15" y1="15" x2="21" y2="21" stroke="#777" stroke-width="2.5"/></svg>
</header>

<section class="hero">
  <svg class="hero-photo" width="1200" height="585" role="img" aria-label="Photo of a team meeting around a table">
    <defs><linearGradient id="heroPhoto" x1="0" y1="0" x2="1" y2="1"><stop offset="0" stop-color="#d9d4cc"/><stop offset=".5" stop-color="#b89f86"/><stop offset="1" stop-color="#6f6a66"/></linearGradient></defs>
    <path d="M790 0 Q660 300 880 585 L1200 585 L1200 0 Z" fill="url(#heroPhoto)"/>
  </svg>
  <h1>We delivering<br>digital infrastructure for<br>Revenue Operations</h1>
  <div class="slider-arrow prev"><svg width="14" height="20"><path d="M11 2 L3 10 L11 18" fill="none" stroke="#fff" stroke-width="2.5"/></svg></div>
  <div class="slider-arrow next"><svg width="14" height="20"><path d="M3 2 L11 10 L3 18" fill="none" stroke="#fff" stroke-width="2.5"/></svg></div>
</section>

<section class="problem">
  <div class="lifecycle-label" style="left:73px;top:198px">CUSTOMER LIFECYCLE <svg width="40" height="8"><line x1="0" y1="4" x2="36" y2="4" stroke="#666" stroke-width="1.5"/><path d="M32 1 L38 4 L32 7" fill="none" stroke="#666" stroke-width="1.5"/></svg></div>
  <div class="stage" style="left:73px"><div class="top" style="background:var(--purple)">Marketing</div><div class="bottom">Marketing Ops</div></div>
  <div class="stage" style="left:242px"><div class="top" style="background:var(--blue)">Sales</div><div class="bottom">Sales Ops</div></div>
  <div class="stage" style="left:409px"><div class="top" style="background:var(--green)">Customer<br>Success</div><div class="bottom">Customer Ops</div></div>
  <svg class="flow-arrow" style="left:214px" width="44" height="10"><line x1="0" y1="5" x2="38" y2="5" stroke="#fff" stroke-width="1.5" stroke-dasharray="4 3"/><path d="M34 1 L42 5 L34 9" fill="none" stroke="#fff" stroke-width="1.5"/></svg>
  <svg class="flow-arrow" style="left:382px" width="44" height="10"><line x1="0" y1="5" x2="38" y2="5" stroke="#fff" stroke-width="1.5" stroke-dasharray="4 3"/><path d="M34 1 L42 5 L34 9" fill="none" stroke="#fff" stroke-width="1.5"/></svg>

  <h2 class="section-title" style="left:623px;top:84px">The<br>Problem</h2>
  <p class="lead" style="left:623px;top:248px;width:520px">Most companies have legacy org structures based on how businesses were run twenty years ago. New functions have been added into this structure over time, creating leadership roles that are overly broad.</p>
  <p class="lead" style="left:623px;top:443px;width:520px">RevOps consolidates operations into one team to simplify everything.</p>

  <div class="feature" style="left:61px;top:600px">
    <svg width="84" height="84" viewBox="0 0 84 84"><g fill="none" stroke="var(--red)" stroke-width="3"><circle cx="38" cy="44" r="18"/><circle cx="38" cy="44" r="7"/><path d="M38 20v-6M38 74v-6M14 44H8M68 44h-6M21 27l-4-4M59 65l-4-4M21 61l-4 4M59 23l-4 4"/><circle cx="68" cy="16" r="6"/></g></svg>
    <h3>MANAGEMENT SKILLS GAP</h3>
    <p>Lorem ipsum dolor sit amet, te veri suscipit expetendis nec, eirmod torquatos per eu. Eu nobis qualisque vim. Te sed eruditi nominavi, cu doming noster platonem mei, facilisi conse quntur eos id.</p>
    <span class="more">LEARN MORE</span>
  </div>
  <div class="feature" style="left:434px;top:600px">
    <svg width="96" height="84" viewBox="0 0 96 84"><g fill="none" stroke="var(--green)" stroke-width="3"><circle cx="48" cy="12" r="7"/><path d="M38 36a10 10 0 0 1 20 0"/><circle cx="18" cy="48" r="7"/><path d="M6 74a12 12 0 0 1 24 0"/><circle cx="78" cy="48" r="7"/><path d="M66 74a12 12 0 0 1 24 0"/><path d="M48 36v12M48 48L22 38M48 48l26-10"/><rect x="36" y="56" width="24" height="18"/></g></svg>
    <h3>MULTIPLE EVERYTHING</h3>
    <p>Lorem ipsum dolor sit amet, te veri suscipit expetendis nec, eirmod torquatos per eu. Eu nobis qualisque vim. Te sed eruditi nominavi, cu doming noster platonem mei, facilisi conse quntur eos id.</p>
    <span class="more">LEARN MORE</span>
  </div>
  <div class="feature" style="left:809px;top:600px">
    <svg width="100" height="98" viewBox="0 0 100 98"><g fill="none" stroke-width="3"><rect x="24" y="2" width="40" height="44" stroke="#1a6f8a"/><path d="M32 14h24M32 24h24M32 34h16" stroke="#1a6f8a"/><path d="M4 96V50M14 96V60M28 96V66h10v30M46 96V58h10v38M64 96V70h10v26M82 96V78h10v18M0 96h100" stroke="var(--orange)"/></g></svg>
    <h3>FUZZY REPORTING RELATIONSHIPS</h3>
    <p>Lorem ipsum dolor sit amet, te veri suscipit expetendis nec, eirmod torquatos per eu. Eu nobis qualisque vim. Te sed eruditi nominavi, cu doming noster platonem mei, facilisi conse quntur eos id.</p>
    <span class="more">LEARN MORE</span>
  </div>
</section>

<section class="target">
  <div class="target-photo" role="img" aria-label="Photo of a customer working on a laptop in a library"></div>
  <h2>Target<br>Customer</h2>
  <p>We firmly believes that the end user should always be the center of attention. While developing and implementing any process, the team must be laser-focused on making the end user's job easier and faster. So our team constantly engages AEs to discover pain points and inefficient workflows that inhibit timely response to customers. The team also relentlessly looks for ways to push information to help AEs increase sales, such as algorithm-generated recommendations on sales automation apps and related products.</p>
</section>

<section class="value">
  <h2 class="section-title" style="left:61px;top:105px">Value<br>Proposition</h2>
  <p class="lead" style="left:61px;top:289px;width:520px;line-height:36px">Apart from acquisition, the paradigm-shift in how revenue flows adds three more revenue drivers&nbsp; to maximize the revenue potential would be to achieve sustenance, and prepare for scale with consistent and delightful customer experience.</p>

  <div class="lifecycle-label" style="left:626px;top:148px">CUSTOMER LIFECYCLE <svg width="40" height="8"><line x1="0" y1="4" x2="36" y2="4" stroke="#666" stroke-width="1.5"/><path d="M32 1 L38 4 L32 7" fill="none" stroke="#666" stroke-width="1.5"/></svg></div>
  <div class="cycle-box" style="left:626px;top:185px;width:257px;height:96px;background:var(--blue);font-size:22px">Sales</div>
  <div class="cycle-box" style="left:883px;top:185px;width:256px;height:96px;background:var(--green);font-size:22px">Customer Success</div>
  <div class="cycle-box" style="left:626px;top:281px;width:513px;height:81px;background:var(--purple);font-size:22px">Marketing</div>
  <div class="cycle-box" style="left:626px;top:362px;width:513px;height:43px;background:var(--red);font-size:13px;font-weight:500">Revenue Operations</div>

  <div class="feature" style="left:57px;top:568px">
    <svg width="76" height="112" viewBox="0 0 76 112"><g fill="none" stroke-width="3"><path d="M36 36C20 34 12 22 14 8c14 0 22 10 22 28zM40 36c2-16 12-24 28-22-2 14-12 22-28 22z" stroke="var(--green)"/><circle cx="36" cy="76" r="34" stroke="var(--red)"/><path d="M12 60c10 4 14 12 10 22-2 6 4 12 8 16M46 46c-4 8 4 12 10 12s12 8 8 16" stroke="var(--red)"/></g></svg>
    <h3 style="margin-top:28px">SUSTENANCE</h3>
    <p>Lorem ipsum dolor sit amet, te veri suscipit expetendis nec, eirmod torquatos per eu. Eu nobis qualisque vim. Te sed eruditi nominavi, cu doming noster platonem mei, facilisi conse quntur eos id.</p>
    <span class="more">LEARN MORE</span>
  </div>
  <div class="feature" style="left:434px;top:568px">
    <svg width="100" height="112" viewBox="0 0 100 112"><g fill="none" stroke-width="3"><path d="M4 56l24-22 14 12 30-26" stroke="var(--orange)"/><path d="M62 18h12v12" stroke="var(--orange)"/><path d="M10 110V82h10v28M30 110V72h10v38M50 110V64h10v46M70 110V52h10v58M2 110h96" stroke="var(--green)"/></g></svg>
    <h3 style="margin-top:28px">GROWTH STRATEGIES</h3>
    <p>Lorem ipsum dolor sit amet, te veri suscipit expetendis nec, eirmod torquatos per eu. Eu nobis qualisque vim. Te sed eruditi nominavi, cu doming noster platonem mei, facilisi conse quntur eos id.</p>
    <span class="more">LEARN MORE</span>
  </div>
  <div class="feature" style="left:809px;top:568px">
    <svg width="100" height="112" viewBox="0 0 100 112"><g fill="none" stroke-width="3"><path d="M14 26l3 7 7 1-5 5 1 7-6-3-6 3 1-7-5-5 7-1zM50 10l3 7 7 1-5 5 1 7-6-3-6 3 1-7-5-5 7-1zM86 26l3 7 7 1-5 5 1 7-6-3-6 3 1-7-5-5 7-1z" stroke="var(--red)"/><circle cx="50" cy="58" r="13" stroke="#1a6f8a"/><path d="M26 110V92c0-12 10-20 24-20s24 8 24 20v18" stroke="#1a6f8a"/></g></svg>
    <h3 style="margin-top:28px">CUSTOMER EXPERIENCE</h3>
    <p>Lorem ipsum dolor sit amet, te veri suscipit expetendis nec, eirmod torquatos per eu. Eu nobis qualisque vim. Te sed eruditi nominavi, cu doming noster platonem mei, facilisi conse quntur eos id.</p>
    <span class="more">LEARN MORE</span>
  </div>
</section>

<section class="benefits">
  <h2>Benefits</h2>
  <div class="benefit-card" style="left:61px;top:314px;width:516px;height:269px">
    <h3>Marketing Intelligence</h3>
    <p>Attribution to campaigns – understand and double down on the ones that create a delta.</p>
  </div>
  <div class="benefit-card" style="left:619px;top:310px;width:522px;height:271px">
    <h3>Simplified Sales Workflows</h3>
    <p>Create sales documents (and gather sign-offs) including service contracts or SLAs, master service agreements.</p>
  </div>
  <div class="card-arrow" style="left:515px"><svg width="14" height="20"><path d="M11 2 L3 10 L11 18" fill="none" stroke="#fff" stroke-width="2.5"/></svg></div>
  <div class="card-arrow" style="left:605px"><svg width="14" height="20"><path d="M3 2 L11 10 L3 18" fill="none" stroke="#fff" stroke-width="2.5"/></svg></div>
</section>

<footer class="site-footer">
  <div class="brand"><span class="brand-mark"></span>loomtrax.io</div>
  <nav class="foot-nav"><span>Home</span><span>Services</span><span>Resources</span><span>Blog</span><span>Contact Us</span></nav>
  <div class="copy">©Copyright information here</div>
</footer>

</body>
</html>
```